Vr holdings enterprise pty ltd

2 sided card black and red with white
Very professional and elegant

Target Market(s)

Construction and Development

Industry/Entity Type

Construction and development

Contact Information for Business Card

One side black, one side red/or white business logo in top corner, email: morgan@vrholdingsgroup.example

Requirements
Should not have
• Blue

```html
<!DOCTYPE html>
<html lang="en">
<head>
<meta charset="utf-8">
<title>VR Holdings – Business Card</title>
<link href="https://fonts.googleapis.com/css2?family=Raleway:wght@300;400;700;800&display=swap" rel="stylesheet">
<style>
  :root {
    --page: #eeeeee;
    --black: #000000;
    --red: #fb0d0d;
    --white: #ffffff;
    --shadow: rgba(0, 0, 0, 0.28);
  }
  * { margin: 0; padding: 0; box-sizing: border-box; }
  html, body {
    width: 1200px;
    height: 1000px;
    overflow: hidden;
    background: var(--page);
    font-family: "Raleway", sans-serif;
  }
  .canvas { position: relative; width: 1200px; height: 1000px; }

  .card {
    position: absolute;
    left: 249px;
    width: 703px;
    height: 422px;
    box-shadow: 0 3px 10px var(--shadow);
    overflow: hidden;
  }
  .card--front { top: 56px; background: var(--black); }
  .card--back { top: 523px; background: var(--red); }

  /* brand name lockup */
  .brand {
    position: absolute;
    display: flex;
    align-items: center;
    justify-content: center;
    gap: 12px;
    color: var(--white);
    font-weight: 800;
    letter-spacing: 0.04em;
    white-space: nowrap;
  }
  .brand__mark { background: var(--red); flex: none; }
  .card--front .brand {
    left: 0; right: 0; top: 150px;
    font-size: 52px;
  }
  .card--front .brand__mark { width: 18px; height: 18px; }

  /* website frame */
  .web-rule {
    position: absolute;
    top: 315px;
    height: 3px;
    background: var(--white);
  }
  .web-rule--left { left: 0; width: 143px; }
  .web-rule--right { left: 560px; width: 143px; }
  .web-box {
    position: absolute;
    left: 143px; top: 291px;
    width: 418px; height: 52px;
    border: 3px solid var(--white);
    display: flex; align-items: center; justify-content: center;
    color: var(--white);
    font-weight: 300;
    font-size: 22px;
    letter-spacing: 0.01em;
  }

  /* back side */
  .band-dark {
    position: absolute;
    left: 0; top: 49px;
    width: 294px; height: 98px;
    background: var(--black);
  }
  .band-light {
    position: absolute;
    left: 294px; top: 49px;
    width: 409px; height: 98px;
    background: var(--white);
  }
  .band-dark .brand {
    inset: 0;
    font-size: 28px;
    gap: 8px;
  }
  .band-dark .brand__mark { width: 10px; height: 10px; }

  .person {
    position: absolute;
    left: 50px; top: 166px;
    color: var(--white);
  }
  .person__name {
    font-weight: 700;
    font-size: 38px;
    line-height: 1;
    letter-spacing: 0.01em;
  }
  .person__role {
    margin-top: 10px;
    font-weight: 400;
    font-size: 14px;
    text-transform: uppercase;
  }

  .contact {
    position: absolute;
    left: 0; right: 0; top: 299px;
    display: flex; align-items: center; justify-content: center;
    gap: 10px;
    color: var(--white);
  }
  .contact__icon { width: 34px; height: 34px; flex: none; }
  .contact__email { font-weight: 300; font-size: 28px; }
  .contact-rule {
    position: absolute;
    left: 229px; top: 342px;
    width: 245px; height: 3px;
    background: var(--white);
  }
</style>
</head>
<body>
<main class="canvas">

  <section class="card card--front" aria-label="Card front">
    <div class="brand">VR HOLDINGS<span class="brand__mark"></span></div>
    <div class="web-rule web-rule--left"></div>
    <div class="web-box">WWW.YOURWEBSITE.COM</div>
    <div class="web-rule web-rule--right"></div>
  </section>

  <section class="card card--back" aria-label="Card back">
    <div class="band-dark">
      <div class="brand">VR HOLDINGS<span class="brand__mark"></span></div>
    </div>
    <div class="band-light"></div>

    <div class="person">
      <p class="person__name">YOUR NAME</p>
      <p class="person__role">Your Profession</p>
    </div>

    <div class="contact">
      <svg class="contact__icon" viewBox="0 0 34 34" aria-hidden="true">
        <circle cx="17" cy="17" r="17" fill="#ffffff"/>
        <rect x="9" y="11" width="16" height="12" fill="none" stroke="#fb0d0d" stroke-width="1.6"/>
        <polyline points="9,11 17,18 25,11" fill="none" stroke="#fb0d0d" stroke-width="1.6"/>
      </svg>
      <span class="contact__email">morgan@vrholdingsgroup.example</span>
    </div>
    <div class="contact-rule"></div>
  </section>

</main>
</body>
</html>
```